mh ridgeline excursions website for fish guide business in Campbell river Bc

looking for website to promote my fishing guide buisiness and its charters

Have uploaded a pictures of my boat not sure which one…
Also two pictures of a fish caught and one of a fish cleaning station

Have added script for website

Target Market(s)

Visitors to Campbell River BC who want fish and or go whale / wildlife adventure tour

Industry/Entity Type

Tourism

Coding

Coded - Design and coding required

Number of Pages Required

5+ page

Font styles to use
Sans Serif

Requirements
Must have
• New email is info@mhridgelineexcursions…. Delete the word halibut…. Add second contact Wes 2507316924….Pictures and my logo … place for videos
Should not have
• should not have a boat picture which is not supplied

```html
<!DOCTYPE html>
<html lang="en">
<head>
<meta charset="utf-8">
<title>MH Ridgeline Excursions – Campbell River Fishing Charters</title>
<link href="https://fonts.googleapis.com/css2?family=Roboto:wght@400;500;700;900&display=swap" rel="stylesheet">
<style>
:root{
  --stage:#17090c;
  --navy:#2a2466;
  --ink:#1d1f3e;
  --muted:#5a5d75;
  --line:#e4e5ec;
  --orange:#e57b1e;
  --footer:#2b2d36;
  --footer-text:#9ea1ad;
  --white:#ffffff;
  --soft:#f5f5f7;
  --teal:#1b5c5a;
}
*{box-sizing:border-box;margin:0;padding:0}
html,body{width:1200px;height:2832px;overflow:hidden}
body{background:var(--stage);font-family:Roboto,Arial,sans-serif;color:var(--ink);position:relative}
.abs{position:absolute}
.photo{position:absolute}
.nowrap{white-space:nowrap}

/* scene tones used for photo areas */
.tone-marina{background:
  radial-gradient(ellipse 38% 22% at 62% 62%,rgba(230,232,238,.75),rgba(230,232,238,0) 70%),
  radial-gradient(ellipse 30% 35% at 20% 30%,rgba(120,70,60,.55),rgba(120,70,60,0) 70%),
  radial-gradient(ellipse 35% 30% at 85% 20%,rgba(90,110,70,.6),rgba(90,110,70,0) 70%),
  linear-gradient(180deg,#4a5548 0%,#3a4658 45%,#2d4a66 75%,#1c2a40 100%)}
.tone-angler{background:
  radial-gradient(ellipse 22% 30% at 42% 45%,rgba(40,80,180,.75),rgba(40,80,180,0) 70%),
  radial-gradient(ellipse 25% 28% at 75% 62%,rgba(120,190,130,.7),rgba(120,190,130,0) 70%),
  radial-gradient(ellipse 30% 25% at 25% 75%,rgba(200,200,205,.8),rgba(200,200,205,0) 70%),
  linear-gradient(180deg,#9fb6c8 0%,#5f7d6a 12%,#3f7aa0 30%,#4d86a6 60%,#8a8a86 88%,#5a5048 100%)}
.tone-dock{background:
  radial-gradient(ellipse 40% 25% at 45% 65%,rgba(240,242,245,.85),rgba(240,242,245,0) 70%),
  radial-gradient(ellipse 50% 20% at 50% 10%,rgba(40,50,70,.8),rgba(40,50,70,0) 70%),
  linear-gradient(180deg,#2a3550 0%,#4e6888 35%,#b8c3cf 62%,#7c95b3 80%,#5a7698 100%)}
.tone-video{background:
  radial-gradient(ellipse 45% 30% at 48% 70%,rgba(210,212,230,.45),rgba(210,212,230,0) 70%),
  radial-gradient(ellipse 30% 25% at 15% 20%,rgba(150,100,90,.4),rgba(150,100,90,0) 70%),
  linear-gradient(170deg,#5a5a86 0%,#3d3a78 50%,#2e2c66 100%)}
.tone-cta{background:
  radial-gradient(ellipse 40% 25% at 50% 60%,rgba(190,192,200,.35),rgba(190,192,200,0) 70%),
  radial-gradient(ellipse 30% 25% at 25% 25%,rgba(110,90,70,.4),rgba(110,90,70,0) 70%),
  linear-gradient(180deg,#3b3d48 0%,#2a2d3c 45%,#34405a 75%,#222636 100%)}

/* desktop */
.desktop{position:absolute;left:20px;top:22px;width:956px;height:2791px;background:var(--white);overflow:hidden}
.topbar{height:27px;border-bottom:1px solid var(--line);position:relative;font-size:9px;color:var(--muted)}
.topbar span{position:absolute;top:8px;letter-spacing:.5px;white-space:nowrap}
.pill-tag{background:#eceef3;padding:2px 6px;border-radius:2px;top:6px!important;font-size:8px}
.header{height:88px;position:relative;border-bottom:1px solid var(--line)}
.logo-mark{position:absolute;border:2px solid var(--navy);border-radius:50%;display:flex;align-items:center;justify-content:center;text-align:center;font-weight:700;color:var(--navy);line-height:1.05}
.navlink{position:absolute;font-size:10px;color:var(--ink);white-space:nowrap}
.appt{position:absolute;right:144px;top:30px;text-align:right;font-size:7px;color:var(--orange);white-space:nowrap}
.appt b{display:block;font-size:11px;font-weight:700}
.hero{height:449px;position:relative;color:var(--white);text-align:center}
.hero h1{position:absolute;left:0;right:0;top:94px;font-size:50px;font-weight:700;line-height:60px}
.hero p{position:absolute;left:0;right:0;top:292px;font-size:12px;line-height:15px}
.btn-white{position:absolute;left:419px;top:343px;width:118px;height:44px;background:var(--white);color:var(--ink);font-size:9px;letter-spacing:1px;display:flex;align-items:center;justify-content:center}
.hero small{position:absolute;left:0;right:0;top:400px;font-size:9px}
.vision{height:435px;position:relative}
.eyebrow{font-size:7px;font-weight:700}
.vision h2{font-size:26px;line-height:30px;font-weight:500;margin:10px 0 14px}
.body{font-size:9.5px;line-height:17px;color:var(--muted)}
.tick{display:flex;align-items:center;gap:8px;font-size:9.5px;font-weight:500;margin-top:8px}
.btn-navy{background:var(--navy);color:var(--white);font-size:9px;letter-spacing:1px;display:inline-flex;align-items:center;justify-content:center;white-space:nowrap}
.events{height:540px;position:relative;text-align:center}
.events h2{position:absolute;left:0;right:0;top:40px;font-size:24px;font-weight:500;color:var(--navy)}
.events .lead{position:absolute;left:0;right:0;top:84px;font-size:10.5px;line-height:16px;color:var(--navy)}
.card{position:absolute;left:116px;top:141px;width:723px;height:254px;border:1px solid var(--line);text-align:left}
.pager{position:absolute;left:60px;top:195px;display:flex;gap:18px;align-items:center;font-size:12px}
.pager small{font-size:8px}
.pill-outline{position:absolute;left:351px;top:431px;width:253px;height:37px;border-radius:19px;background:#eef0f3;font-size:9.5px;letter-spacing:1px;color:var(--navy);display:flex;align-items:center;justify-content:center;gap:8px}
.video-band{height:286px;position:relative}
.play{position:absolute;border:2px solid var(--white);border-radius:50%;display:flex;align-items:center;justify-content:center}
.testimonials{height:313px;background:var(--soft);text-align:center;position:relative}
.testimonials h2{position:absolute;left:0;right:0;top:78px;font-size:24px;font-weight:500}
.testimonials blockquote{position:absolute;left:280px;width:400px;top:124px;font-size:13.5px;line-height:24px;font-weight:500}
.cta{height:358px;position:relative;color:var(--white);text-align:center}
.cta h2{position:absolute;left:0;right:0;top:70px;font-size:40px;line-height:46px;font-weight:700}
.cta p{position:absolute;left:0;right:0;top:188px;font-size:14px;line-height:19px}
.footer{height:294px;background:var(--footer);position:relative;color:var(--white)}
.fcol{position:absolute;top:64px;font-size:9px}
.fcol h4{font-size:7px;font-weight:700;color:var(--footer-text);letter-spacing:.6px;margin-bottom:14px}
.fcol li{list-style:none;margin-bottom:11px;white-space:nowrap}
.flogo{position:absolute;background:var(--white);display:flex;align-items:center;justify-content:center;color:var(--navy);font-weight:700;text-align:center}
.social{display:flex;gap:14px}
.social i{width:13px;height:13px;background:var(--white);display:block;border-radius:2px}
.legal{display:flex;gap:18px;white-space:nowrap}

/* mobile */
.mobile{position:absolute;left:1004px;top:22px;width:177px;height:2401px;background:var(--white);overflow:hidden}
.m-header{height:47px;position:relative}
.m-hero{height:296px;position:relative;color:var(--white);text-align:center}
.m-hero h1{position:absolute;left:8px;right:8px;top:50px;font-size:26px;line-height:31px;font-weight:700}
.m-hero p{position:absolute;left:14px;right:14px;top:186px;font-size:7px;line-height:10px}
.m-vision{height:345px;padding:5px 9px;position:relative}
.m-vision h2{font-size:18px;line-height:22px;font-weight:500;margin:6px 0 6px}
.m-body{font-size:6px;line-height:11px;color:var(--muted)}
.m-events{height:574px;position:relative;text-align:center}
.m-video{height:127px;position:relative}
.m-testi{height:201px;position:relative;text-align:center}
.m-cta{height:252px;position:relative;color:var(--white);padding:30px 8px}
.m-footer{height:559px;background:var(--footer);position:relative;color:var(--white);font-size:6px}
</style>
</head>
<body>

<main class="desktop">
  <div class="topbar">
    <span class="pill-tag" style="left:121px">Special Offer</span>
    <span style="left:200px">JOIN THE IT CAMPAIGN.</span>
    <span style="left:350px">&#9742;&nbsp; Phone: +1 250 555 0173</span>
    <span style="left:686px">English &#709;</span>
    <span style="left:750px">HELP CENTER</span>
  </div>

  <header class="header">
    <div class="logo-mark" style="left:136px;top:26px;width:36px;height:36px;font-size:5px">MH<br>RIDGELINE</div>
    <nav>
      <span class="navlink" style="left:317px;top:38px">Home</span>
      <span class="navlink" style="left:367px;top:38px">About</span>
      <span class="navlink" style="left:417px;top:38px">Services List &#709;</span>
      <span class="navlink" style="left:509px;top:38px">events</span>
      <span class="navlink" style="left:561px;top:38px">Blog</span>
      <span class="navlink" style="left:606px;top:38px">Contact</span>
    </nav>
    <div class="appt">call for appointment<b>+ 1 250 555 0173</b></div>
    <svg class="abs" style="left:830px;top:37px" width="13" height="13" viewBox="0 0 13 13"><circle cx="5.5" cy="5.5" r="4" fill="none" stroke="#1d1f3e" stroke-width="2"/><path d="M8.5 8.5 12 12" stroke="#1d1f3e" stroke-width="2"/></svg>
  </header>

  <section class="hero">
    <div class="photo tone-marina" role="img" aria-label="Charter boat moored at the Campbell River marina" style="inset:0"></div>
    <div class="photo" style="inset:0;background:rgba(31,29,74,.45)"></div>
    <h1>Experience the<br>Ultimate West Coast<br>Adventure:</h1>
    <p>Welcome aboard the 22-foot Harbourline charter boat, where MH Ridgeline<br>Excursions and the legendary Cal Brennan</p>
    <div class="btn-white">BOOK NOW</div>
    <small>Or call us at 250 555 0188</small>
  </section>

  <section class="vision">
    <div class="photo tone-angler" role="img" aria-label="Angler holding a fishing rod aboard the charter boat on calm water" style="left:107px;top:45px;width:377px;height:319px;box-shadow:0 10px 24px rgba(0,0,0,.2)"></div>
    <div class="abs" style="left:595px;top:40px;width:245px">
      <div class="eyebrow">Company's vision</div>
      <h2>Discover Your Thrilling West Coast Adventure - Book Your Charter Today!</h2>
      <p class="body">Welcome aboard the 22-foot Harbourline charter boat, where MH Ridgeline Excursions and the legendary Cal Brennan await to take you on an unforgettable journey through the untamed beauty of Campbell River.</p>
      <div class="tick" style="margin-top:16px"><svg width="10" height="8"><path d="M1 4l3 3 5-6" fill="none" stroke="#1d1f3e" stroke-width="1.2"/></svg>Reel in Your Dream Catch</div>
      <div class="tick"><svg width="10" height="8"><path d="M1 4l3 3 5-6" fill="none" stroke="#1d1f3e" stroke-width="1.2"/></svg>Awe-Inspiring Wildlife Moments</div>
      <div style="display:flex;align-items:center;gap:14px;margin-top:22px">
        <span class="btn-navy" style="width:138px;height:37px">SEE HOW WE WORK</span>
        <span style="font-size:9.5px;color:var(--navy);white-space:nowrap">(250) 555-0142</span>
      </div>
    </div>
    <div class="abs" style="left:897px;top:250px;width:28px;height:28px;border-radius:50%;background:#fff;box-shadow:0 2px 8px rgba(0,0,0,.15);font-size:10px;display:flex;align-items:center;justify-content:center">&#708;</div>
    <nav class="sticky-nav" style="color:var(--muted)">
      <span class="navlink" style="left:317px;top:369px;font-size:9.5px">Home</span>
      <span class="navlink" style="left:367px;top:369px;font-size:9.5px">About</span>
      <span class="navlink" style="left:417px;top:369px;font-size:9.5px">Services List &#709;</span>
      <span class="navlink" style="left:509px;top:369px;font-size:9.5px">events</span>
      <span class="navlink" style="left:561px;top:369px;font-size:9.5px">Blog</span>
    </nav>
  </section>

  <section class="events">
    <h2>Our Events</h2>
    <p class="lead">Don't miss out on this epic adventure - time is running out! The<br>demand for our charters is soaring, and spots are filling up fast.</p>
    <div class="card">
      <p class="body" style="position:absolute;left:54px;top:40px;width:255px;font-size:10.5px;line-height:17px">With Cal Brennan's expert guidance, you'll have the chance to reel in monstrous salmon, massive lingcod, and feisty cod. Prepare for an angler's dream come true as you witness the sheer power and excitement of landing your prized catch</p>
      <div class="abs" style="left:54px;top:160px;font-size:9.5px">Cal Brennan</div>
      <div class="pager"><span>&#8249;</span><small>1 – 4</small><span>&#8250;</span></div>
      <div class="photo tone-dock" role="img" aria-label="Anglers working on the charter boat at the dock" style="left:361px;top:0;width:361px;height:253px"></div>
    </div>
    <div class="pill-outline">EXPERIENCE THE SOUL OF OCEAN <span>&#8250;</span></div>
  </section>

  <section class="video-band">
    <div class="photo tone-video" role="img" aria-label="Video still of the charter boat at the marina" style="inset:0"></div>
    <svg class="abs" style="left:0;top:200px" width="956" height="86" viewBox="0 0 956 86" preserveAspectRatio="none"><path d="M0 0 Q478 150 956 0 V86 H0Z" fill="#f5f5f7"/></svg>
    <div class="play" style="left:450px;top:108px;width:55px;height:55px"><svg width="14" height="14"><path d="M3 1l10 6-10 6z" fill="#fff"/></svg></div>
  </section>

  <section class="testimonials">
    <h2>Testimonials</h2>
    <blockquote>Wes, Chief Designer — “Hub began as a collaborative architectural and landscape workshop, and has remained true to its trans-disciplinary way of thinking since its inception.”</blockquote>
    <span class="abs" style="left:262px;top:170px;font-size:14px;color:var(--muted)">&#8592;</span>
    <span class="abs" style="left:683px;top:170px;font-size:14px">&#8594;</span>
    <div class="abs" style="left:392px;top:245px;font-size:7px;color:var(--muted)">01</div>
    <div class="abs" style="left:415px;top:249px;width:120px;height:1px;background:#cfd1d9"></div>
    <div class="abs" style="left:555px;top:245px;font-size:7px;color:var(--muted)">05</div>
  </section>

  <section class="cta">
    <div class="photo tone-cta" role="img" aria-label="Charter boat tied up at the dock" style="inset:0"></div>
    <div class="photo" style="inset:0;background:rgba(20,22,40,.35)"></div>
    <h2>Book Your Thrilling<br>Charter Today!</h2>
    <p>Your heart-pounding West Coast adventure is just a call away! Grab<br>your phone and dial 250-555-0148</p>
    <span class="btn-navy abs" style="left:424px;top:245px;width:92px;height:36px">BOOK NOW</span>
  </section>

  <footer class="footer">
    <div class="flogo" style="left:116px;top:64px;width:72px;height:58px;font-size:9px;border-radius:2px">MH<br>Ridgeline</div>
    <p class="abs" style="left:116px;top:146px;width:150px;font-size:8.5px;line-height:16px;color:var(--footer-text)">Welcome aboard the 22-foot Harbourline charter boat, where MH Ridgeline</p>
    <div class="social abs" style="left:116px;top:198px"><i></i><i></i><i></i></div>
    <div class="fcol" style="left:293px"><h4>COMPANY</h4><ul><li>About Us</li><li>Careers</li><li>Press</li><li>Blog and Media</li><li>Sectors</li><li>Our Projects</li></ul></div>
    <div class="fcol" style="left:410px"><h4>SUPPORT</h4><ul><li>Home</li><li>About</li><li>Services List &#709;</li><li>events</li><li>Contact</li></ul></div>
    <div class="fcol" style="left:528px"><h4>NEED HELP?</h4>
      <div style="font-size:8px;color:#6e7180;white-space:nowrap">Toll Free Customer Care</div>
      <div style="font-size:11px;margin-top:4px;white-space:nowrap">+(1) 250 555 0190</div>
      <div style="font-size:8px;color:#6e7180;margin-top:40px;white-space:nowrap">Need live support?</div>
      <div style="font-size:9px;margin-top:4px;white-space:nowrap">info@mhridgelineexcursions</div>
    </div>
    <div class="fcol" style="left:660px"><h4>KEEP IN TOUCH</h4>
      <div style="width:180px;height:34px;background:#353845;border-radius:4px;position:relative;font-size:9px;color:#a4a7b4;padding:11px 12px">Email address
        <span style="position:absolute;right:8px;top:5px;width:38px;height:24px;border-radius:12px;background:var(--teal);display:flex;align-items:center;justify-content:center;color:#fff">&#8250;</span></div>
    </div>
    <div class="legal abs" style="left:116px;top:247px;font-size:8.5px"><span>English</span><span>Privacy Policy</span><span>Contact</span></div>
    <div class="abs nowrap" style="left:732px;top:247px;font-size:8px;color:var(--footer-text)">© 2023 All Rights Reserved</div>
  </footer>
</main>

<main class="mobile">
  <header class="m-header">
    <svg class="abs" style="left:8px;top:12px" width="9" height="9"><circle cx="3.8" cy="3.8" r="2.8" fill="none" stroke="#1d1f3e" stroke-width="1.3"/><path d="M6 6l2.5 2.5" stroke="#1d1f3e" stroke-width="1.3"/></svg>
    <div class="logo-mark" style="left:78px;top:8px;width:20px;height:20px;font-size:4px;border-width:1.5px">MH</div>
    <svg class="abs" style="left:162px;top:13px" width="9" height="7"><path d="M0 .5h9M0 3.5h9M0 6.5h9" stroke="#1d1f3e"/></svg>
  </header>
  <section class="m-hero">
    <div class="photo tone-marina" role="img" aria-label="Charter boat moored at the Campbell River marina" style="inset:0"></div>
    <div class="photo" style="inset:0;background:rgba(31,29,74,.45)"></div>
    <h1>Experience the Ultimate West Coast Adventure:</h1>
    <p>Welcome aboard the 22-foot Harbourline charter boat, where MH Ridgeline Excursions and the legendary Cal Brennan</p>
    <div class="abs" style="left:45px;top:233px;width:87px;height:30px;background:#fff;color:var(--ink);font-size:6px;display:flex;align-items:center;justify-content:center">BOOK NOW</div>
    <div class="abs" style="left:0;right:0;top:275px;font-size:5.5px">Or call us at 250 555 0188</div>
  </section>
  <section class="m-vision">
    <div style="font-size:5px;font-weight:700">Company's vision</div>
    <h2>Discover Your Thrilling West Coast Adventure - Book Your Charter Today!</h2>
    <p class="m-body">Welcome aboard the 22-foot Harbourline charter boat, where MH Ridgeline Excursions and the legendary Cal Brennan await to take you on an unforgettable journey through the untamed beauty of Campbell River.</p>
    <div class="m-body" style="margin-top:8px;color:var(--ink)">&#10003; Reel in Your Dream Catch<br>&#10003; Awe-Inspiring Wildlife Moments</div>
    <div class="btn-navy" style="width:101px;height:27px;font-size:5px;margin-top:10px">SEE HOW WE WORK</div>
    <div style="font-size:5px;margin-top:6px">(250) 555-0142</div>
  </section>
  <section class="m-events">
    <div style="position:absolute;left:0;right:0;top:0;font-size:16px;font-weight:500;color:var(--navy)">Our Events</div>
    <p class="m-body" style="position:absolute;left:9px;right:9px;top:24px;line-height:10px">Don't miss out on this epic adventure - time is running out! The demand for our charters is soaring, and spots are filling up fast.</p>
    <div class="abs" style="left:9px;top:82px;width:161px;height:185px;border:1px solid var(--line);text-align:left;padding:22px 8px">
      <p class="m-body" style="line-height:10px">With Cal Brennan's expert guidance, you'll have the chance to reel in monstrous salmon, massive lingcod, and feisty cod. Prepare for an angler's dream come true as you witness the sheer power and excitement of landing your prized catch</p>
      <div style="font-size:5px;margin-top:12px">Cal Brennan</div>
    </div>
    <div class="photo tone-dock" role="img" aria-label="Anglers working on the charter boat at the dock" style="left:9px;top:272px;width:161px;height:184px"></div>
    <div class="abs" style="left:9px;top:487px;width:170px;height:26px;border-radius:13px;background:#eef0f3;font-size:5.5px;letter-spacing:.5px;color:var(--navy);display:flex;align-items:center;justify-content:center;white-space:nowrap">EXPERIENCE THE SOUL OF OCEAN &#8250;</div>
  </section>
  <section class="m-video">
    <div class="photo tone-video" role="img" aria-label="Video still of the charter boat at the marina" style="inset:0"></div>
    <svg class="abs" style="left:0;top:80px" width="177" height="47" viewBox="0 0 177 47" preserveAspectRatio="none"><path d="M0 0 Q88 90 177 0 V47 H0Z" fill="#fff"/></svg>
    <div class="play" style="left:70px;top:32px;width:38px;height:38px"><svg width="10" height="10"><path d="M2 1l7 4-7 4z" fill="#fff"/></svg></div>
  </section>
  <section class="m-testi">
    <div style="position:absolute;left:0;right:0;top:18px;font-size:16px;font-weight:500">Testimonials</div>
    <p style="position:absolute;left:12px;right:12px;top:52px;font-size:7px;line-height:17px;font-weight:500">Wes, Chief Designer — “Hub began as a collaborative architectural and landscape workshop, and has remained true to its trans-disciplinary way of thinking since its inception.”</p>
  </section>
  <section class="m-cta">
    <div class="photo tone-cta" role="img" aria-label="Charter boat tied up at the dock" style="inset:0"></div>
    <div style="position:relative;font-size:20px;line-height:26px;font-weight:700">Book Your Thrilling Charter Today!</div>
    <p style="position:relative;font-size:9.5px;line-height:13px;margin-top:8px">Your heart-pounding West Coast adventure is just a call away! Grab your phone and dial 250-555-0148</p>
    <div class="btn-navy" style="position:relative;width:66px;height:27px;font-size:5.5px;margin:18px 0 0 44px">BOOK NOW</div>
  </section>
  <footer class="m-footer">
    <div class="flogo" style="left:9px;top:46px;width:70px;height:42px;font-size:7px">MH Ridgeline</div>
    <p class="abs" style="left:9px;top:104px;width:160px;color:var(--footer-text);line-height:10px">Welcome aboard the 22-foot Harbourline charter boat, where MH Ridgeline Excursions</p>
    <div class="social abs" style="left:9px;top:143px;gap:10px"><i style="width:9px;height:9px"></i><i style="width:9px;height:9px"></i><i style="width:9px;height:9px"></i></div>
    <div class="abs nowrap" style="left:9px;top:178px;line-height:16px"><div style="font-size:4.5px;color:var(--footer-text)">COMPANY</div>About Us<br>Careers<br>Press<br>Blog and Media<br>Terms &amp; Conditions<br>Sectors<br>Our Projects</div>
    <div class="abs nowrap" style="left:93px;top:178px;line-height:16px"><div style="font-size:4.5px;color:var(--footer-text)">SUPPORT</div>Home<br>About<br>Services List &#709;<br>events<br>Blog<br>Contact</div>
    <div class="abs nowrap" style="left:9px;top:328px;line-height:11px"><div style="font-size:4.5px;color:var(--footer-text)">NEED HELP?</div><span style="color:#6e7180">Toll Free Customer Care</span><br>+(1) 250 555 0190<br><br><span style="color:#6e7180">Need live support?</span><br>info@mhridgelineexcursions</div>
    <div class="abs" style="left:9px;top:433px;font-size:4.5px;color:var(--footer-text)">KEEP IN TOUCH</div>
    <div class="abs" style="left:9px;top:452px;width:160px;height:18px;border-bottom:1px solid #4a4d5a;color:#a4a7b4;padding-top:4px">Email address</div>
    <div class="abs" style="left:129px;top:450px;width:40px;height:14px;border-radius:7px;background:var(--teal)"></div>
    <div class="legal abs" style="left:0;right:0;top:489px;justify-content:center;gap:8px;font-size:5px"><span>English</span><span>Privacy Policy</span><span>Contact</span></div>
    <div class="abs" style="left:0;right:0;top:510px;text-align:center;font-size:5px;color:var(--footer-text)">© 2023 All Rights Reserved</div>
  </footer>
</main>

</body>
</html>
```